BEREAN FELLOWSHIP GLOBAL.

THIS IS A PRAISE AND WORSHIP MEETING, WORTH NOTING, THAT ITS OUR FIRST MEETING. OUR THEME AND VISION......" Creating a platform for Interaction between Man and God". This should stand out. We also have a logo and I will email it to the designer that takes the job. We will have three pictures on the flier. Red is favourite color........ DATE OF THE MEETING. Saturday NOV 11th 2017. 6:30pm-9pm. Venue STILLWATER HARVEST CHAPEL 48260 Juniper Crest Ave, Auburn Wa 98347. Punch line at the bottom.....' the PRAISE to be'

Target Market(s)

Youth and adults.

Industry/Entity Type

Performing Art

Font styles to use
Decorative

Colors

Designer to choose colors to be used in the design.

Requirements
Must have
• The first design of the attached Logo. And the words......CREATING A PLATFORM FOR INTERACTION BETWEEN MAN AND GOD.
Should not have
• Pictures of three individuals. I have one but waiting for 2. I can send them later. The picture that is attached is of Samuel T Odhiambo.

```html
<!DOCTYPE html>
<html lang="en">
<head>
<meta charset="utf-8">
<title>Berean Fellowship Global – Praise Meeting Flyer</title>
<link href="https://fonts.googleapis.com/css2?family=Cinzel:wght@400;600&family=Crimson+Text:wght@400;600&family=Oswald:wght@500&family=Montserrat:wght@500&display=swap" rel="stylesheet">
<style>
  :root {
    --stage: #4b4b4b;
    --paper: #ffffff;
    --red: #c8353b;
    --charcoal: #312e30;
    --black: #141414;
    --placeholder: #c6c6c6;
    --ink: #2b2b2b;
  }
  html, body {
    margin: 0;
    width: 1200px;
    height: 1200px;
    overflow: hidden;
    background: var(--stage);
  }
  .flyer {
    position: absolute;
    left: 200px;
    top: 37px;
    width: 800px;
    height: 1126px;
    background: var(--paper);
    box-shadow: 0 6px 24px rgba(0,0,0,.35);
  }
  .flyer svg { display: block; width: 100%; height: 100%; overflow: hidden; }
  .corner-red, .band-red, .footer-red { fill: var(--red); }
  .corner-dark { fill: var(--charcoal); }
  .band-black { fill: var(--black); }
  .portrait-slot { fill: var(--placeholder); }
  .rule-dark { stroke: var(--ink); stroke-width: 1; }
  .rule-light { stroke: var(--paper); stroke-width: .8; }
  .brand-name { font-family: 'Cinzel', serif; font-weight: 400; font-size: 9.5px; fill: var(--ink); letter-spacing: .3px; }
  .brand-dot { fill: var(--red); }
  .theme-line { font-family: 'Cinzel', serif; font-weight: 400; font-size: 12.5px; fill: var(--paper); text-anchor: middle; }
  .theme-main { font-family: 'Cinzel', serif; font-weight: 400; font-size: 18px; fill: var(--paper); text-anchor: middle; letter-spacing: .5px; }
  .event-date { font-family: 'Crimson Text', serif; font-weight: 600; font-size: 15.5px; fill: var(--paper); }
  .event-time { font-family: 'Oswald', sans-serif; font-weight: 500; font-size: 30px; fill: var(--paper); }
  .icon { fill: none; stroke: var(--red); stroke-width: 1.3; }
  .venue { font-family: 'Montserrat', sans-serif; font-weight: 500; font-size: 7.2px; fill: var(--paper); }
  .punchline { font-family: 'Cinzel', serif; font-weight: 400; font-size: 12.5px; fill: var(--paper); text-anchor: middle; letter-spacing: .4px; }
</style>
</head>
<body>
<main class="flyer">
  <svg viewBox="0 0 430 605" xmlns="http://www.w3.org/2000/svg" preserveAspectRatio="none">
    <polygon class="corner-red" points="0,0 172,0 0,172"/>
    <polygon class="corner-dark" points="255,0 430,0 430,178"/>

    <g class="portraits">
      <rect class="portrait-slot" role="img" aria-label="Portrait placeholder for guest minister" x="31" y="160" width="142" height="142" rx="12" transform="rotate(45 102 231)"/>
      <rect class="portrait-slot" role="img" aria-label="Portrait placeholder for guest minister" x="259" y="160" width="142" height="142" rx="12" transform="rotate(45 330 231)"/>
      <defs>
        <linearGradient id="stageGlow" x1="0" y1="0" x2="1" y2="1">
          <stop offset="0" stop-color="#8a7fd6"/>
          <stop offset=".45" stop-color="#3e3b52"/>
          <stop offset="1" stop-color="#6b6478"/>
        </linearGradient>
      </defs>
      <rect role="img" aria-label="Photo of the featured minister smiling on stage" fill="url(#stageGlow)" x="139" y="36" width="158" height="158" rx="12" transform="rotate(45 218 115)"/>
    </g>

    <g class="brand">
      <circle class="brand-dot" cx="155" cy="325" r="9"/>
      <text class="brand-name" x="170" y="320">BEREAN FELLOWSHIP</text>
      <text class="brand-name" x="170" y="331">GLOBAL</text>
    </g>

    <line class="rule-dark" x1="215" y1="361" x2="430" y2="361"/>

    <rect class="band-red" x="0" y="368" width="430" height="64"/>
    <text class="theme-line" x="215" y="389">CREATING A PLATFORM FOR INTERACTION</text>
    <text class="theme-main" x="215" y="413">BETWEEN MAN AND GOD</text>
    <line class="rule-light" x1="0" y1="425" x2="203" y2="425"/>

    <polygon class="band-black" points="0,446 310,446 385,530 0,530"/>
    <g class="icon">
      <rect x="39" y="461" width="17" height="15" rx="1.5"/>
      <line x1="39" y1="466" x2="56" y2="466"/>
      <line x1="43" y1="459" x2="43" y2="463"/>
      <line x1="52" y1="459" x2="52" y2="463"/>
      <circle cx="47.5" cy="506" r="8.5"/>
      <polyline points="43.5,506 46.5,509 52,502"/>
    </g>
    <text class="event-date" x="71" y="473">Saturday NOV 11th 2017</text>
    <text class="event-time" x="71" y="517">6:30PM–9PM</text>

    <polygon class="footer-red" points="95,532 430,532 430,598 45,598"/>
    <path d="M123,546 a4.5,4.5 0 1 1 9,0 c0,3.5 -4.5,8.5 -4.5,8.5 s-4.5,-5 -4.5,-8.5z" fill="#ffffff"/>
    <circle cx="127.5" cy="546" r="1.6" fill="var(--red)"/>
    <text class="venue" x="139" y="551">STILLWATER HARVEST CHAPEL 48260 Juniper Crest Ave,</text>
    <text class="venue" x="139" y="562">Auburn Wa 98347</text>
    <line class="rule-light" x1="60" y1="584" x2="145" y2="584"/>
    <text class="punchline" x="237" y="589">THE PRAISE TO BE</text>
    <line class="rule-light" x1="330" y1="584" x2="430" y2="584"/>
  </svg>
</main>
</body>
</html>
```